Brisk Mark Lab atendeu e superou minhas expectativas. Usando os canais oferecidos, tive a possibilidade de atingir com relação à logomarca de nossa empresa.

```html
<!DOCTYPE html>
<html lang="pt-BR">
<head>
<meta charset="UTF-8">
<title>Cartão de visitas – Aerofall Academy</title>
<link href="https://fonts.googleapis.com/css2?family=Montserrat:wght@400;600;700&display=swap" rel="stylesheet">
<style>
  :root {
    --backdrop: #2b2b2d;
    --card-light: #ffffff;
    --card-dark: #1c1c1e;
    --gold: #b8964f;
    --ink: #3a3a3a;
    --ink-soft: #7a7a7a;
    --silver: #d9d9d9;
  }
  * { box-sizing: border-box; margin: 0; padding: 0; }
  html, body {
    width: 1200px; height: 1200px; overflow: hidden;
    background: var(--backdrop);
    font-family: "Montserrat", sans-serif;
  }
  .stage {
    width: 1200px; height: 1200px;
    display: flex; flex-direction: column; align-items: center; justify-content: center;
    gap: 60px;
  }
  .card {
    width: 800px; height: 444px;
    position: relative;
    box-shadow: 0 10px 30px rgba(0,0,0,.45);
  }
  .card--front { background: var(--card-light); display: flex; }
  .card--back { background: var(--card-dark); }

  .brand {
    display: flex; flex-direction: column; align-items: center; gap: 14px;
  }
  .brand__mark {
    width: 46px; height: 46px; border-radius: 50%;
    background: var(--gold);
  }
  .brand__name {
    font-weight: 700; font-size: 34px; letter-spacing: 3px;
    color: var(--gold); text-transform: uppercase; text-align: center; line-height: 1.1;
  }
  .brand__tagline {
    font-weight: 600; font-size: 11px; letter-spacing: 3px;
    color: var(--ink-soft); text-transform: uppercase; white-space: nowrap;
  }
  .card--back .brand__tagline { color: var(--silver); }

  .front__brand-area {
    width: 50%; display: flex; align-items: center; justify-content: center;
  }
  .front__details {
    width: 50%; padding: 90px 40px 0 20px;
  }
  .holder__name {
    font-weight: 700; font-size: 18px; letter-spacing: 1.5px; color: var(--ink);
    text-transform: uppercase;
  }
  .holder__role {
    font-size: 12px; color: var(--gold); margin-top: 4px; margin-bottom: 26px;
  }
  .contact { list-style: none; display: flex; flex-direction: column; gap: 13px; }
  .contact__item {
    display: flex; align-items: center; gap: 12px;
    font-size: 12px; color: var(--ink); line-height: 1.35;
  }
  .contact__icon {
    flex: none; width: 22px; height: 22px; border-radius: 50%;
    background: var(--gold); display: flex; align-items: center; justify-content: center;
  }
  .contact__icon svg { width: 12px; height: 12px; }
  .contact__item--web { font-weight: 700; color: var(--gold); letter-spacing: .5px; }

  .back__brand-area {
    position: absolute; right: 70px; top: 120px;
  }
</style>
</head>
<body>
<main class="stage">
  <section class="card card--front">
    <div class="front__brand-area">
      <div class="brand">
        <span class="brand__mark"></span>
        <span class="brand__name">Aerofall<br>Academy</span>
        <span class="brand__tagline">Focus · Training · Flight</span>
      </div>
    </div>
    <div class="front__details">
      <p class="holder__name">Nome Sobrenome</p>
      <p class="holder__role">Instrutor de Voo</p>
      <ul class="contact">
        <li class="contact__item">
          <span class="contact__icon"><svg viewBox="0 0 12 12"><path d="M2 1h2.5l1 2.5-1.5 1a6 6 0 0 0 3.5 3.5l1-1.5L11 7.5V10a1 1 0 0 1-1 1A9 9 0 0 1 1 2a1 1 0 0 1 1-1z" fill="#fff"/></svg></span>
          +55 (00) 0000-0000
        </li>
        <li class="contact__item">
          <span class="contact__icon"><svg viewBox="0 0 12 12"><rect x="3" y="1" width="6" height="10" rx="1" fill="none" stroke="#fff" stroke-width="1.2"/></svg></span>
          +55 (00) 00000-0000
        </li>
        <li class="contact__item">
          <span class="contact__icon"><svg viewBox="0 0 12 12"><rect x="1" y="2.5" width="10" height="7" fill="none" stroke="#fff" stroke-width="1.2"/><path d="M1 2.5l5 4 5-4" fill="none" stroke="#fff" stroke-width="1.2"/></svg></span>
          nome@aerofallacademy.com
        </li>
        <li class="contact__item">
          <span class="contact__icon"><svg viewBox="0 0 12 12"><path d="M6 11S2 6.8 2 4.5a4 4 0 0 1 8 0C10 6.8 6 11 6 11z" fill="#fff"/><circle cx="6" cy="4.5" r="1.4" fill="#b8964f"/></svg></span>
          <span>Rua Exemplo, 100, Centro<br>CEP 00000-000 · Cidade</span>
        </li>
        <li class="contact__item contact__item--web">
          <span class="contact__icon"><svg viewBox="0 0 12 12"><circle cx="6" cy="6" r="4.6" fill="none" stroke="#fff" stroke-width="1.2"/><path d="M1.4 6h9.2M6 1.4c2.4 2.6 2.4 6.6 0 9.2M6 1.4c-2.4 2.6-2.4 6.6 0 9.2" fill="none" stroke="#fff" stroke-width="1"/></svg></span>
          www.aerofallacademy.com
        </li>
      </ul>
    </div>
  </section>

  <section class="card card--back">
    <div class="back__brand-area">
      <div class="brand">
        <span class="brand__mark"></span>
        <span class="brand__name">Aerofall<br>Academy</span>
        <span class="brand__tagline">Focus · Training · Flight</span>
      </div>
    </div>
  </section>
</main>
</body>
</html>
```